Larkfell PowerPoint Slide Deck

We have created a new company the provides workforce solutions for rural healthcare providers in the United States. We have a website located at: https://larkfellsolutions.example. Now we need a PowerPoint template that Larkfell employees can use to support in-person and virtual presentations. We want the final PowerPoint template/master slides to be consistent thematically with the Larkfell website, with an emphasis on simplicity -- clean, subtle, professional, relatively stark and with a white background dominant. It should use the Larkfell color scheme, logo and logo pattern. The product we select will need a cover/title slide as well as templates for a variety of slide layouts. Please refer to the Larkfell Style Guide attached to this request.

```html
<!DOCTYPE html>
<html lang="en">
<head>
<meta charset="utf-8">
<title>Larkfell Presentation Slides</title>
<link rel="stylesheet" href="https://fonts.googleapis.com/css2?family=Montserrat:wght@400;500;700&display=swap">
<style>
  :root {
    --red: #e01b14;
    --dark: #1f0b0c;
    --ink: #161616;
    --white: #ffffff;
    --pattern-a: #d8474a;
    --pattern-b: #eea3a3;
    --photo-a: #c9d3dd;
    --photo-b: #8a9bb0;
  }
  * { margin: 0; padding: 0; box-sizing: border-box; }
  html, body { width: 1200px; height: 400px; overflow: hidden; background: var(--white); }
  body { position: relative; font-family: "Montserrat", sans-serif; color: var(--ink); }

  .slide {
    position: absolute; top: 55px; width: 521px; height: 293px;
    background: var(--white); overflow: hidden;
    box-shadow: 0 4px 18px rgba(0,0,0,0.12);
  }
  .slide--cover { left: 65px; }
  .slide--content { left: 612px; }

  .pattern-band { position: absolute; background: linear-gradient(135deg, var(--pattern-a), var(--pattern-b) 50%, var(--pattern-a)); }
  .photo { position: absolute; }

  /* Cover slide */
  .cover__red-block { position: absolute; left: 0; top: 0; width: 214px; height: 44px; background: var(--red); }
  .cover__dark-block { position: absolute; left: 13px; top: 22px; width: 184px; height: 53px; background: var(--dark); }
  .cover__pattern-side { left: 0; top: 8px; width: 25px; height: 285px; }
  .cover__pattern-base { left: 0; top: 285px; width: 118px; height: 8px; }
  .cover__photo { left: 25px; top: 44px; width: 233px; height: 241px;
    background: linear-gradient(160deg, var(--photo-a), var(--photo-b) 60%, #2c3446); }

  .brand { position: absolute; display: flex; align-items: center; gap: 8px; }
  .brand__square { width: 29px; height: 29px; background: var(--red); }
  .brand__name { font-weight: 700; font-size: 20px; color: var(--ink); }
  .cover__brand { left: 385px; top: 22px; }

  .cover__title { position: absolute; left: 295px; top: 106px; font-weight: 700; font-size: 20px; line-height: 23.5px; color: var(--ink); }
  .accent { color: var(--red); }
  .cover__presenter { position: absolute; left: 295px; top: 205px; width: 136px; height: 27px;
    background: var(--dark); color: var(--white); font-size: 9.5px; display: flex; align-items: center; justify-content: center; }
  .cover__presenter strong { font-weight: 700; margin-left: 3px; }
  .cover__date { position: absolute; left: 296px; top: 258px; font-weight: 700; font-size: 10px; }

  /* Content slide */
  .content__photo { left: 0; top: 0; width: 521px; height: 149px;
    background: linear-gradient(100deg, #3d4a63, #9eb4c8 45%, #c7d7e4 70%, #7c95b0); }
  .content__pattern { left: 0; top: 137px; width: 230px; height: 18px; }
  .content__title { position: absolute; left: 33px; top: 167px; font-weight: 700; font-size: 20px; }
  .content__body { position: absolute; left: 35px; top: 194px; width: 410px; font-size: 10px; line-height: 11.8px; }
  .content__footer-meta { position: absolute; left: 34px; top: 250px; font-size: 10px; line-height: 9.5px; }
  .content__footer-meta strong { display: block; font-weight: 700; }
  .content__rule { position: absolute; left: 172px; top: 260px; width: 193px; height: 1.5px; background: var(--dark); }
  .content__brand { left: 386px; top: 246px; }
</style>
</head>
<body>
  <section class="slide slide--cover">
    <div class="cover__red-block"></div>
    <div class="cover__dark-block"></div>
    <div class="pattern-band cover__pattern-side" role="img" aria-label="Larkfell brand pattern border"></div>
    <div class="pattern-band cover__pattern-base" role="img" aria-label="Larkfell brand pattern border"></div>
    <div class="photo cover__photo" role="img" aria-label="Photo of a healthcare executive with medical staff in the background"></div>

    <div class="brand cover__brand">
      <span class="brand__square"></span>
      <span class="brand__name">Larkfell</span>
    </div>

    <h1 class="cover__title">Empowering<br>Rural Healthcare<br>Organizations with<br><span class="accent">Tailored Solutions</span></h1>
    <div class="cover__presenter">Presented By <strong>Jane Doe</strong></div>
    <p class="cover__date">October 30th, 2025</p>
  </section>

  <section class="slide slide--content">
    <div class="photo content__photo" role="img" aria-label="Photo of healthcare professionals attending a presentation"></div>
    <div class="pattern-band content__pattern" role="img" aria-label="Larkfell brand pattern band"></div>

    <h2 class="content__title">Tailored Solutions for <span class="accent">Rural Hospitals</span></h2>
    <p class="content__body">At Larkfell, we’re dedicated to supporting rural hospitals and healthcare providers with personalized insurance, retirement, and workforce solutions—<span class="accent">helping you care for your teams as much as you care for your patients.</span></p>

    <div class="content__footer-meta">
      <strong>Presented By Jane Doe</strong>
      October 30th, 2025
    </div>
    <div class="content__rule"></div>
    <div class="brand content__brand">
      <span class="brand__square"></span>
      <span class="brand__name">Larkfell</span>
    </div>
  </section>
</body>
</html>
```